Bref créative
Corvale Power Associates, LLC
Stationery and business cards
Professional
Dean Halvorsen
President
28715 Birchwood Crest Lane
Suite 615
Linden Park, TX 77519
dean.halvorsen@corvale-pa.com
We will need multiple name, cell phone, and email changes. Primary colors should be white, black, and a vibrant blue.
Here is our logo Ai.

```html
<!DOCTYPE html>
<html lang="en">
<head>
<meta charset="utf-8">
<title>Corvale Power Associates — Stationery</title>
<link href="https://fonts.googleapis.com/css2?family=Montserrat:wght@400;600;700&display=swap" rel="stylesheet">
<style>
  :root {
    --blue: #1479e0;
    --blue-deep: #0a4fa8;
    --blue-bright: #3aa0ff;
    --ink: #1a1a1a;
    --grey: #6d6d6d;
    --paper: #ffffff;
    --backdrop: #e6e8eb;
    --faint: #eef3fa;
  }
  * { box-sizing: border-box; margin: 0; padding: 0; }
  html, body { width: 1200px; height: 742px; overflow: hidden; }
  body {
    position: relative;
    background: var(--backdrop);
    font-family: "Montserrat", sans-serif;
    color: var(--ink);
  }
  .sheet, .envelope, .card {
    position: absolute;
    background: var(--paper);
    overflow: hidden;
    box-shadow: 0 2px 6px rgba(0,0,0,.18);
  }
  .brand {
    display: flex; align-items: center; gap: 8px;
    font-weight: 700; color: var(--blue); white-space: nowrap;
  }
  .brand__dot { border-radius: 50%; background: var(--blue); flex: none; }
  .brand--white { color: var(--paper); }
  .brand--white .brand__dot { background: var(--paper); }

  .watermark { position: absolute; border-radius: 50%; background: var(--faint); }

  /* Letterheads */
  .letterhead { top: 72px; width: 432px; height: 606px; }
  .letterhead--plain { left: 168px; }
  .letterhead--swoosh { left: 636px; width: 463px; }
  .letterhead .brand { position: absolute; left: 24px; top: 26px; font-size: 18px; }
  .letterhead .brand__dot { width: 22px; height: 22px; }
  .letterhead .watermark { width: 220px; height: 220px; left: 50%; top: 300px; transform: translateX(-50%); }
  .letterhead__footer {
    position: absolute; left: 0; right: 0; bottom: 16px;
    text-align: center; font-size: 5px; line-height: 1.6; color: var(--grey);
  }
  .letterhead__rule {
    position: absolute; left: 60px; right: 60px; bottom: 36px; height: 1px; background: #cfcfcf;
  }
  .letterhead__wave { position: absolute; left: 0; bottom: 0; width: 463px; height: 112px; }
  .letterhead--swoosh .letterhead__footer {
    text-align: left; left: 26px; bottom: 10px; color: var(--paper);
  }

  /* Envelopes */
  .envelope--front { left: 533px; top: 312px; width: 391px; height: 228px; }
  .envelope--front .envelope__band { position: absolute; right: 0; top: 0; width: 90px; height: 228px; }
  .envelope__return {
    position: absolute; left: 14px; top: 146px; font-size: 7px; line-height: 1.5; color: var(--ink);
  }
  .envelope--back { left: 396px; top: 247px; width: 336px; height: 209px; box-shadow: 0 3px 8px rgba(0,0,0,.25); }
  .envelope__flap { position: absolute; left: 0; top: 0; width: 336px; height: 112px; }
  .envelope--back .brand { position: absolute; left: 112px; top: 20px; font-size: 14px; gap: 6px; }
  .envelope--back .brand__dot { width: 14px; height: 14px; }
  .envelope--back .watermark { width: 100px; height: 100px; left: 118px; top: 104px; }

  /* Business cards */
  .card--front { left: 79px; top: 247px; width: 168px; height: 72px; border-radius: 4px; }
  .card--back {
    left: 79px; top: 348px; width: 168px; height: 84px; border-radius: 4px;
    background: linear-gradient(135deg, var(--blue-bright), var(--blue) 55%, var(--blue-deep));
  }
  .card .brand { position: absolute; font-size: 8px; gap: 4px; }
  .card .brand__dot { width: 9px; height: 9px; }
  .card--front .brand { top: 7px; left: 10px; }
  .card--back .brand { top: 36px; left: 14px; font-size: 10px; }
  .card__band { position: absolute; right: 0; top: 0; width: 36px; height: 72px; }
  .card__details {
    position: absolute; left: 36px; top: 22px; font-size: 4.6px; line-height: 1.45; color: var(--ink);
  }
  .card__name { font-weight: 600; font-size: 5.4px; }
</style>
</head>
<body>

  <section class="sheet letterhead letterhead--plain">
    <div class="brand"><span class="brand__dot"></span>Corvale Power Associates</div>
    <div class="watermark" aria-hidden="true"></div>
    <div class="letterhead__rule"></div>
    <p class="letterhead__footer">
      28715 Birchwood Crest Lane, Suite 615 · Linden Park, TX 77519<br>
      Phone 713.555.0142 · Fax 713.555.0143 · corvale-pa.com
    </p>
  </section>

  <section class="sheet letterhead letterhead--swoosh">
    <div class="brand"><span class="brand__dot"></span>Corvale Power Associates</div>
    <div class="watermark" aria-hidden="true"></div>
    <svg class="letterhead__wave" viewBox="0 0 463 112" preserveAspectRatio="none" aria-hidden="true">
      <defs>
        <linearGradient id="waveBlue" x1="0" x2="1">
          <stop offset="0" stop-color="#0a4fa8"/>
          <stop offset="0.6" stop-color="#1479e0"/>
          <stop offset="1" stop-color="#3aa0ff"/>
        </linearGradient>
      </defs>
      <path d="M0 72 C140 90 310 72 463 10 L463 112 L0 112 Z" fill="url(#waveBlue)"/>
      <path d="M0 66 C140 84 310 66 463 4" fill="none" stroke="#1a1a1a" stroke-width="2"/>
    </svg>
    <p class="letterhead__footer">
      28715 Birchwood Crest Lane, Suite 615 · Linden Park, TX 77519<br>
      Phone 713.555.0142 · Fax 713.555.0143 · corvale-pa.com
    </p>
  </section>

  <section class="envelope envelope--front">
    <svg class="envelope__band" viewBox="0 0 90 228" preserveAspectRatio="none" aria-hidden="true">
      <path d="M90 0 L50 0 C76 70 76 160 44 228 L90 228 Z" fill="#1479e0"/>
      <path d="M42 0 C68 70 68 160 36 228" fill="none" stroke="#1a1a1a" stroke-width="2"/>
    </svg>
    <p class="envelope__return">
      28715 Birchwood Crest Lane, Suite 615<br>
      Linden Park, TX 77519
    </p>
  </section>

  <section class="envelope envelope--back">
    <div class="watermark" aria-hidden="true"></div>
    <svg class="envelope__flap" viewBox="0 0 336 112" preserveAspectRatio="none" aria-hidden="true">
      <defs>
        <linearGradient id="flapBlue" x1="0" x2="1">
          <stop offset="0" stop-color="#0a4fa8"/>
          <stop offset="0.5" stop-color="#3aa0ff"/>
          <stop offset="1" stop-color="#0a4fa8"/>
        </linearGradient>
      </defs>
      <path d="M0 0 L336 0 L336 10 L180 106 Q168 112 156 106 L0 10 Z" fill="url(#flapBlue)"/>
    </svg>
    <div class="brand brand--white"><span class="brand__dot"></span>Corvale</div>
  </section>

  <section class="card card--front">
    <div class="brand"><span class="brand__dot"></span>Corvale</div>
    <div class="card__details">
      <p class="card__name">Dean Halvorsen</p>
      <p>President</p>
      <p>28715 Birchwood Crest Lane, Suite 615</p>
      <p>Linden Park, TX 77519</p>
      <p>Cell 713.555.0187</p>
      <p>dean.halvorsen@corvale-pa.com</p>
    </div>
    <svg class="card__band" viewBox="0 0 36 72" preserveAspectRatio="none" aria-hidden="true">
      <path d="M36 0 L18 0 C31 24 31 48 15 72 L36 72 Z" fill="#1479e0"/>
    </svg>
  </section>

  <section class="card card--back">
    <div class="brand brand--white"><span class="brand__dot"></span>Corvale</div>
  </section>

</body>
</html>
```